Tidewell Consulting Schedule Of Rates

We need a brochure / proposal for our new company. Our company is a start up based in Australia who provides engineering and sales support to other renewable energy companies. Our brochure is a pitch-deck / sales item that catalogues our key services. We are engineering consultants.

Our website is www.tidewellpartners.com.au. Please review the website to get a feel of colour schemes etc.

We are looking for a strong, trustworthy feel, but the brochure also needs to be sales driven and to the point.

The second page that contains the $30 price point needs to be loud and clear.

The use of relevant icons throughout the document will be viewed favorably.

Please format the tables to look attractive.

The document will need to be in an editable format so content can be edited by us at a later date.

Please feel free to use the pics within the attached word document. The winning design will be provided with updated, clearer images upon request.

Thank you

Target Market(s)

Businesses that either sell or install solar PV and other renewable energy systems in Australia. Most of target market are likely to be electrical contractors.

Industry/Entity Type

Engineering

Colors
0255a3
0492cd
ffffff

Requirements
Must have
• Icons, graphics presentation, Clean and Clear, Business oriented. Sharp sales feel
Nice to have
• solar picture backgrounds maybe
Should not have
• cartoons, over sales driven,

```html
<!DOCTYPE html>
<html lang="en">
<head>
<meta charset="utf-8">
<title>Tidewell Consulting – Schedule of Rates</title>
<link href="https://fonts.googleapis.com/css2?family=Roboto+Condensed:wght@300;400;700&display=swap" rel="stylesheet">
<style>
:root{
  --navy:#0255a3;
  --blue:#0492cd;
  --band:#2a95d3;
  --white:#ffffff;
  --ink:#2b2b2b;
  --stage:#4a4a4b;
}
*{box-sizing:border-box;margin:0;padding:0}
html,body{width:1132px;height:1200px;overflow:hidden;background:var(--stage)}
body{font-family:"Roboto Condensed",Arial,sans-serif;color:var(--ink);position:relative}
.page{position:absolute;width:344px;height:487px;background:var(--white);overflow:hidden}
.p1{left:188px;top:79px}
.p2{left:600px;top:79px}
.p3{left:188px;top:634px;height:486px}
.p4{left:600px;top:634px;height:486px}

.brand{position:absolute;font-weight:700;color:#111;letter-spacing:-.2px;white-space:nowrap;display:flex;align-items:center;gap:4px}
.brand .mark{width:8px;height:8px;background:var(--navy);display:inline-block}
.brand-small{right:12px;top:11px;font-size:10px}
.brand-small .mark{width:6px;height:6px}

.footer{position:absolute;left:0;bottom:0;width:100%;height:25px;background:var(--band);display:flex;align-items:center;justify-content:space-between;padding:0 20px 0 21px;color:var(--white);font-size:5.6px}
.p1 .footer{height:36px}
.footer span::before{content:"";display:inline-block;width:3px;height:3px;background:var(--white);margin-right:1.5px;vertical-align:middle}
.p2 .footer{background:rgba(2,85,163,.35)}

/* cover */
.cover-art{position:absolute;inset:0;background:
  linear-gradient(180deg,#eef5fb 0%,#d8e8f4 25%,#cfe2f1 45%,#9fc3e6 52%,#3a7fc8 62%,#2266b4 80%,#4f8fd3 100%)}
.cover-brand{left:0;right:0;top:50px;justify-content:center;font-size:22px}
.cover-tag{position:absolute;top:97px;width:100%;text-align:center;color:var(--blue);font-size:13px;font-weight:300;letter-spacing:-.2px}
.cover-title{position:absolute;top:180px;width:100%;text-align:center;font-size:15px;font-weight:700;color:#333}
.cover-sub{position:absolute;top:199px;width:100%;text-align:center;font-size:9px;color:#333}

/* headings */
.heading{position:absolute;left:36px;border-left:1px solid #333;padding-left:2px;line-height:1}
.heading .h-strong{color:var(--navy);font-weight:700;font-size:14.5px;display:block}
.heading .h-light{color:var(--navy);font-weight:300;font-size:14px;display:block;margin-top:2px}
.p2 .heading .h-light{color:var(--blue);font-size:11.5px}

.bullets{position:absolute;left:37px;top:86px;list-style:none;font-size:7px;line-height:11px;color:#333}
.bullets li::before{content:"";display:inline-block;width:3.5px;height:3.5px;border-radius:50%;background:var(--blue);margin-right:3px;vertical-align:middle}

.price{position:absolute;left:32px;display:flex;align-items:center;gap:5px}
.price .disc{width:34px;height:34px;border-radius:50%;border:1px solid #9fa6ad;display:flex;flex-direction:column;align-items:center;justify-content:center;color:var(--navy);line-height:1}
.price .disc b{font-size:10.5px}
.price .disc small{font-size:6px;margin-top:1px}
.price.lead .disc{background:var(--navy);border-color:var(--navy);color:var(--white)}
.price .info{font-size:7px;line-height:9.5px;color:#333}
.price .info b{font-weight:700}

.photo-round{position:absolute;border-radius:50%;border:2px solid var(--white)}
.roof-a{left:167px;top:107px;width:106px;height:106px;background:radial-gradient(circle at 50% 45%,#c8ced3,#8f989f 70%,#6b7479)}
.roof-b{left:222px;top:190px;width:106px;height:106px;background:radial-gradient(circle at 45% 55%,#a9b3bb,#6f7b84 65%,#4f5a61)}
.install-photo{position:absolute;left:0;top:312px;width:100%;height:175px;background:linear-gradient(180deg,rgba(255,255,255,0) 0%,#c9a79a 38%,#6c83b4 55%,#3e5f9c 80%,#2f4f8c 100%)}

/* tables */
.sub{position:absolute;left:36px;top:91px;font-size:8px;font-weight:700;color:#222}
.block{position:absolute;left:36px;width:273px}
.block h3{font-size:7px;font-weight:700;color:#222;margin-bottom:1px}
.rates{width:100%;border-collapse:collapse;font-size:5.8px;color:#333;table-layout:fixed}
.rates col.c1{width:79px}.rates col.c3{width:63px}
.rates th{background:var(--band);color:var(--white);font-weight:700;height:14px;text-align:left;padding-left:12px;border-left:2px solid var(--white)}
.rates th:first-child{border-left:0}
.rates th.rate{text-align:center;padding-left:0}
.rates td{border:1px solid var(--band);padding:2px 8px;vertical-align:middle;line-height:7.4px}
.rates td.rate{text-align:center;padding:0}
.rates td.desc{padding:3px 2px 2px 3px;line-height:9.8px}
.rates td.desc ul{list-style:none}
.rates td.desc li::before{content:"• "}
.rates tr.gap td{border:0;height:3px;padding:0}
.note{display:flex;justify-content:space-between;font-size:3.6px;line-height:4.2px;margin-top:4px;padding-left:9px;color:#444}
.note .case{font-size:6px;padding-right:14px}
</style>
</head>
<body>

<section class="page p1">
  <div class="cover-art" role="img" aria-label="Photograph of sky and clouds over a blue solar panel array"></div>
  <div class="brand cover-brand"><span class="mark"></span>Tidewell Consulting</div>
  <p class="cover-tag">DESIGN &amp; SUPPORT SERVICES</p>
  <h1 class="cover-title">SCHEDULE OF RATES</h1>
  <p class="cover-sub">Grid and Off Grid 5kW – 10MW</p>
  <footer class="footer"><span>03 9100 4420</span><span>0412 300 718</span><span>sales@tidewellpartners.com.au</span><span>www.tidewellpartners.com.au</span></footer>
</section>

<section class="page p2">
  <div class="brand brand-small"><span class="mark"></span>Tidewell Consulting</div>
  <h2 class="heading" style="top:49px"><span class="h-strong">SERVICES</span><span class="h-light">PROFESSIONAL PANEL LAYOUT</span></h2>
  <ul class="bullets">
    <li>We can layout the panels for a small fee</li>
    <li>Clear &amp; Concise</li>
    <li>Ranging from 5kW – 300kW</li>
  </ul>
  <div class="photo-round roof-a" role="img" aria-label="Aerial view of a commercial roof with solar panels"></div>
  <div class="photo-round roof-b" role="img" aria-label="Aerial view of an industrial roof with solar arrays"></div>
  <div class="install-photo" role="img" aria-label="Photograph of an installer fitting solar panels on a rooftop"></div>

  <div class="price lead" style="top:144px"><div class="disc"><b>$30</b><small>Ex. Gst</small></div><p class="info">Less than <b>30kW</b><br>Skyview Panel Layout</p></div>
  <div class="price" style="top:197px"><div class="disc"><b>$80</b><small>Ex. Gst</small></div><p class="info"><b>31kW - 100kW</b><br>Skyview Panel Layout</p></div>
  <div class="price" style="top:250px"><div class="disc"><b>$150</b><small>Ex. Gst</small></div><p class="info"><b>100kW - 300kW</b><br>Skyview Panel Layout</p></div>
  <div class="price" style="top:304px"><div class="disc"><b>$360</b><small>Ex. Gst</small></div><p class="info"><b>300kW +</b><br>3D Drawings including<br>shading analysis</p></div>

  <footer class="footer"><span>03 9100 4420</span><span>0412 300 718</span><span>sales@tidewellpartners.com.au</span><span>www.tidewellpartners.com.au</span></footer>
</section>

<section class="page p3">
  <div class="brand brand-small"><span class="mark"></span>Tidewell Consulting</div>
  <h2 class="heading" style="top:55px"><span class="h-strong">GRID CONNECTION</span><span class="h-light">SERVICES</span></h2>
  <p class="sub">30Kw - 50kW</p>

  <div class="block" style="top:109px">
    <h3>Westline, Unity Grid</h3>
    <table class="rates"><colgroup><col class="c1"><col><col class="c3"></colgroup>
      <tr><th>Service</th><th></th><th class="rate">Rates</th></tr>
      <tr class="gap"><td colspan="3"></td></tr>
      <tr><td>Network Application<br>&amp; Case Management</td><td class="desc"><ul><li>AC schematic</li><li>Site plan</li><li>Voltage rise study</li><li>Completed paperwork</li><li>Case Management to approval</li></ul></td><td class="rate">$670</td></tr>
    </table>
  </div>

  <div class="block" style="top:200px">
    <h3>Southnet, Harbourgrid</h3>
    <table class="rates"><colgroup><col class="c1"><col><col class="c3"></colgroup>
      <tr><th>Service</th><th></th><th class="rate">Rates</th></tr>
      <tr class="gap"><td colspan="3"></td></tr>
      <tr><td>Network Application<br>&amp; Case Management</td><td class="desc"><ul><li>AC schematic</li><li>Site plan</li><li>Voltage rise study</li><li>Completed paperwork</li><li>Case Management to approval</li></ul></td><td class="rate">$980</td></tr>
      <tr><td>Onsite Commissioning</td><td class="desc"><ul><li>Injection testing &amp; report</li></ul></td><td class="rate">$1350</td></tr>
    </table>
  </div>

  <div class="block" style="top:314px">
    <h3>Northway</h3>
    <table class="rates"><colgroup><col class="c1"><col><col class="c3"></colgroup>
      <tr><th>Service</th><th></th><th class="rate">Rates</th></tr>
      <tr class="gap"><td colspan="3"></td></tr>
      <tr><td style="vertical-align:top;padding-top:20px">Network Application<br>&amp; Case Management</td><td class="desc"><ul><li>AC schematic</li><li>SolarSim &amp; load profile study</li><li>Site plan</li><li>Voltage rise study</li><li>Protection grading study</li><li>Technical report</li><li>Completed paperwork</li><li>Case Management to approval</li></ul></td><td class="rate" style="vertical-align:top;padding-top:20px">$1820</td></tr>
      <tr><td>Onsite Commissioning</td><td class="desc"><ul><li>Injection testing &amp; report</li></ul></td><td class="rate">$1350</td></tr>
    </table>
  </div>

  <footer class="footer"><span>03 9100 4420</span><span>0412 300 718</span><span>sales@tidewellpartners.com.au</span><span>www.tidewellpartners.com.au</span></footer>
</section>

<section class="page p4">
  <div class="brand brand-small"><span class="mark"></span>Tidewell Consulting</div>

  <div class="block" style="top:72px">
    <h3>Saltbush Networks</h3>
    <table class="rates"><colgroup><col class="c1"><col><col class="c3"></colgroup>
      <tr><th>Service</th><th></th><th class="rate">Rates</th></tr>
      <tr class="gap"><td colspan="3"></td></tr>
      <tr><td>Network Application<br>&amp; Case Management</td><td class="desc"><ul><li>AC schematic</li><li>Site plan</li><li>Voltage rise study</li><li>Completed paperwork</li><li>Case Management to approval</li></ul></td><td class="rate">$790</td></tr>
      <tr><td>Onsite Commissioning</td><td class="desc"><ul><li>Commissioning Plan for onsite witness testing</li></ul></td><td class="rate">$550</td></tr>
    </table>
    <div class="note"><span>Power quality measurement<br>&amp; injection testing (if required)</span><span class="case">Case by case</span></div>
  </div>

  <div class="block" style="top:203px">
    <h3>Coastex, Tropicon</h3>
    <table class="rates"><colgroup><col class="c1"><col><col class="c3"></colgroup>
      <tr><th>Service</th><th></th><th class="rate">Rates</th></tr>
      <tr class="gap"><td colspan="3"></td></tr>
      <tr><td style="height:20px">AC design &amp; Voltage<br>rise study</td><td></td><td class="rate">$190</td></tr>
      <tr><td>Network Application<br>&amp; Case Management</td><td class="desc"><ul><li>AC schematic</li><li>Site plan</li><li>Voltage rise study</li><li>Protection grading study</li><li>Technical report</li><li>Completed paper work</li><li>Case Management to approval</li><li>RPEQ certification of design</li></ul></td><td class="rate">$2150</td></tr>
    </table>
  </div>

  <div class="block" style="top:356px">
    <h3>Top End Utilities</h3>
    <table class="rates"><colgroup><col class="c1"><col><col class="c3"></colgroup>
      <tr><th>Service</th><th></th><th class="rate">Rates</th></tr>
      <tr class="gap"><td colspan="3"></td></tr>
      <tr><td>Network Application<br>&amp; Case Management</td><td class="desc"><ul><li>Preliminary Enquiry</li><li>Site plan</li><li>Voltage rise study</li><li>SolarSim simulation &amp; load profile study</li><li>Completed paperwork</li><li>Case Management to approval</li></ul></td><td class="rate" style="vertical-align:top;padding-top:20px">$1400</td></tr>
    </table>
  </div>

  <footer class="footer"><span>03 9100 4420</span><span>0412 300 718</span><span>sales@tidewellpartners.com.au</span><span>www.tidewellpartners.com.au</span></footer>
</section>

</body>
</html>
```